A colourful crystal mystical tapestry

I need an image for my book cover. The title of the book is The Woven Lantern . Below, the subtitle is Along Quiet Rivers. The crystals move from bottom right to one third up the cover and into the middle. Stop below book title. (Book is 9x6). The crystals have to look like a multi-colour tapestry. Real crystals appear like they are gently exploding from the bottom right of the cover. More like movement than rocketships pls. But not a bunch of fragments. More clustered together. The upper cover will be white. They crystals are multi-covered bright - shinning. It can not be a bad AI image. It must be sharp and brilliant - a tapestry of colours. It is a spiritual book so, it needs to feel as such. If another creative idea comes to mind...give it a try.. I am open to something completely different as long as if is a multi-colour adult appealing spiritual unique image- which represents the title well. THANKS in advance.

Target Market(s)

Readers of multi-dimensional stories. ADULTS

Industry/Entity Type

Spirituality. Beautiful interesting intriguing.

Requirements
Nice to have
• It's tapestry, not chaos per say.
Should not have
• Anything crappy space like AI I can easily create. Be unique.

```html
<!DOCTYPE html>
<html lang="en">
<head>
<meta charset="utf-8">
<title>The Woven Lantern — Book Cover</title>
<link rel="stylesheet" href="https://fonts.googleapis.com/css2?family=Cinzel:wght@400;600;700&display=swap">
<style>
  :root {
    --page-bg: #f3f2f3;
    --cover-bg: #ffffff;
    --ink: #0d0d0d;
    --rule: #3a3a3a;
    --gem-red: #d8232f;
    --gem-crimson: #a3123a;
    --gem-gold: #f5c21b;
    --gem-violet: #6a2fb5;
    --gem-blue: #2f6fe0;
    --gem-pink: #e0408a;
    --gem-orange: #f0712a;
  }
  * { margin: 0; padding: 0; box-sizing: border-box; }
  html, body {
    width: 1200px; height: 1200px; overflow: hidden;
    background: var(--page-bg);
  }
  .cover {
    position: absolute; left: 251px; top: 78px;
    width: 698px; height: 1045px;
    background: var(--cover-bg);
    overflow: hidden;
    font-family: "Cinzel", "Times New Roman", serif;
    color: var(--ink);
  }
  .crystal-art {
    position: absolute; inset: 0; width: 100%; height: 100%;
  }
  .title-article {
    position: absolute; top: 62px; left: 0; right: 0;
    display: flex; align-items: center; justify-content: center; gap: 14px;
    font-size: 46px; font-weight: 400; line-height: 1;
  }
  .title-article .rule {
    width: 150px; height: 1px; background: var(--rule);
  }
  .title-article .rule.left { background: linear-gradient(90deg, transparent, var(--rule)); }
  .title-article .rule.right { background: linear-gradient(90deg, var(--rule), transparent); }
  .title-main {
    position: absolute; top: 124px; left: 0; right: 0; text-align: center;
    font-size: 118px; font-weight: 600; line-height: 1; letter-spacing: 2px;
    background: linear-gradient(100deg, var(--gem-red) 0%, var(--gem-orange) 15%, var(--gem-crimson) 30%, var(--gem-pink) 45%, var(--gem-violet) 60%, var(--gem-blue) 70%, var(--gem-pink) 82%, var(--gem-red) 100%);
    -webkit-background-clip: text; background-clip: text;
    color: transparent;
  }
  .title-second {
    position: absolute; top: 250px; left: 0; right: 0; text-align: center;
    font-size: 84px; font-weight: 600; line-height: 1; letter-spacing: 3px;
  }
  .subtitle {
    position: absolute; top: 340px; left: 0; right: 0; text-align: center;
    font-size: 28px; font-weight: 400; letter-spacing: 1px;
  }
  .author {
    position: absolute; top: 963px; left: 0; right: 0; text-align: center;
    font-size: 40px; font-weight: 700; color: #000;
    text-shadow: -2px -2px 0 #fff, 2px -2px 0 #fff, -2px 2px 0 #fff, 2px 2px 0 #fff, 0 0 6px #fff;
  }
</style>
</head>
<body>
  <main class="cover">
    <svg class="crystal-art" viewBox="0 0 698 1045" role="img" aria-label="Cluster of bright multicoloured crystals bursting gently upward from the bottom right corner">
      <defs>
        <linearGradient id="crystal-fill" x1="1" y1="1" x2="0.2" y2="0.3">
          <stop offset="0" stop-color="#c21a33"/>
          <stop offset="0.25" stop-color="#e2402a"/>
          <stop offset="0.45" stop-color="#f4b82a"/>
          <stop offset="0.6" stop-color="#b0245a"/>
          <stop offset="0.75" stop-color="#e98a3a"/>
          <stop offset="1" stop-color="#f6d28a"/>
        </linearGradient>
        <radialGradient id="crystal-glow" cx="0.72" cy="0.9" r="0.35">
          <stop offset="0" stop-color="#5a4be0" stop-opacity="0.75"/>
          <stop offset="1" stop-color="#5a4be0" stop-opacity="0"/>
        </radialGradient>
      </defs>
      <polygon fill="url(#crystal-fill)" points="697,261 633,348 546,404 366,435 273,497 199,590 99,727 50,869 25,969 25,1045 697,1045"/>
      <polygon fill="url(#crystal-glow)" points="697,261 633,348 546,404 366,435 273,497 199,590 99,727 50,869 25,969 25,1045 697,1045"/>
    </svg>

    <div class="title-article">
      <span class="rule left"></span><span>The</span><span class="rule right"></span>
    </div>
    <h1 class="title-main">WOVEN</h1>
    <div class="title-second">LANTERN</div>
    <p class="subtitle">ALONG QUIET RIVERS</p>
    <p class="author">AUTHOR NAME</p>
  </main>
</body>
</html>
```